TheGlowFrame.net

TheGlowFrame.net
Open Globe Snap Salon of pictures of love for all to enjoy
My goal is to create a website that is designed to be an online art gallery of photos that display what love looks like from all over the world. People will submit an image; write a short quote about why their image represents love
I Love THIS website:
http://markwellory.example/
Please create something like this!!!
User Functionality:
Users must be able to do the following:
• Upload one photo
• Write a brief quote
• Share on their social media site
• Other users can like and share posted image
Backend:
• Site owner must be able to choose which images are uploaded. After user uploads image to site, admin will receive notice of the upload, and make sure the image is not unappropriated or spam. That would be the control functionality.
• At the bottom of the site a contact us, that will send e-mail to admin for any user related questions
Design Functionality:
Website should only be one, simple, elegant, page of photos.
Social Media:
Social media buttons should be small, at the corner of each submitted image
I Love THIS website:
http://markwellory.example/
Homepage: I like the layout and design you have now. Each square/image will have the following social media options, friendloop,chirpline,and Snapgrid. Below each photo their will be a caption that described each photo that appears after you hover over the photo, camera equipment, and a link to the photographer's portfolio/website. There will be able 30-40 images at a time on the homepage, 5-7 photographers at a time.
Featured Photographers:
This is the second page of the website. Here there is a bio of the photographers, how to contact them, and where in the world they are from. The photographers will always be on the page even after their work is taken off the homepage. I will insert links to their personal websites under their bio.
Review/Shop:
Here I will be using affiliated marketing to sell cameras, camera accessories, online photo classes, frames. I will not be selling the pictures featured on the homepage, people will be able to buy directly from the photographer.
Selling: I will be using brimhall partners, and tap vault. I will be installing CoinDrift, but all sales will be they third party vendors
Contact Us:
Here people can inquire about becoming a featured photographer, the company, and anything else
Site Requirements:
Email visitors can join the company mail group.
Target Market(s)
photographers, people who like snapgrid, and boardly
Industry/Entity Type
Marketing
Look and feel

```html
<!DOCTYPE html>
<html lang="en">
<head>
<meta charset="utf-8">
<title>TheGlowFrame.net — Marlene Dusktrove</title>
<link rel="stylesheet" href="https://fonts.googleapis.com/css2?family=Lobster&family=Marck+Script&family=Yanone+Kaffeesatz:wght@400;500&family=Exo+2:wght@400&display=swap">
<style>
  :root {
    --ink: #111111;
    --navy: #1f4466;
    --red: #ff0000;
    --white: #ffffff;
    --frame: #0b0b0b;
    --footer: #000000;
    --caption: #f4f4f4;
  }
  * { box-sizing: border-box; margin: 0; padding: 0; }
  html, body { width: 1095px; height: 1200px; overflow: hidden; }
  body { position: relative; font-family: "Yanone Kaffeesatz", sans-serif; background: #f5f6f8; }

  .backdrop {
    position: absolute; inset: 0 0 109px 0;
    background:
      radial-gradient(ellipse 60% 25% at 55% 8%, rgba(255,255,255,.95), rgba(255,255,255,0) 70%),
      linear-gradient(180deg, #ffffff 0%, #f4f2ee 18%, #d9d2c6 28%, #8b8377 38%, #4d4a48 50%, #2f3034 65%, #3a3c42 80%, #26282d 100%);
  }

  .site-header { position: absolute; top: 52px; left: 186px; right: 186px; height: 40px; }
  .brand {
    position: absolute; left: 0; top: 0;
    font-family: "Lobster", cursive; font-size: 34px; color: var(--ink); letter-spacing: .2px;
  }
  .account-nav { position: absolute; right: 0; top: 6px; display: flex; align-items: center; font-family: "Exo 2", sans-serif; font-size: 20px; color: var(--navy); }
  .account-nav .item { display: flex; align-items: center; gap: 5px; padding: 0 8px; }
  .account-nav .item + .item { border-left: 1px solid #9aa7b4; }
  .account-nav svg { width: 12px; height: 8px; }

  .gallery-title {
    position: absolute; top: 192px; left: 0; width: 1095px; text-align: center;
    font-family: "Marck Script", cursive; font-size: 70px; font-weight: 400; color: var(--navy);
  }
  .gallery-title .surname { color: var(--red); }

  .card { position: absolute; width: 184px; }
  .card-frame {
    position: relative; width: 184px; height: 189px;
    border: 4px solid var(--frame); border-radius: 4px; overflow: hidden; background: var(--frame);
  }
  .card-photo { position: absolute; inset: 0; }
  .photo-runner { background: linear-gradient(160deg, #9fc6c9 0%, #c6d9a8 35%, #b99a7a 60%, #8f8a84 100%); }
  .photo-couple { background: linear-gradient(180deg, #3a7fd0 0%, #9cc4ee 40%, #c07a3e 70%, #7c4a28 100%); }
  .photo-garden { background: linear-gradient(180deg, #e7f0df 0%, #8fc04a 35%, #4d6b2d 65%, #2c3a22 100%); }
  .photo-dog { background: linear-gradient(160deg, #f3c36a 0%, #c98d47 40%, #6d5a43 70%, #3b4a3a 100%); }
  .corner-badge { position: absolute; top: -1px; right: -1px; width: 44px; height: 30px; }
  .share-strip {
    position: absolute; left: 0; right: 0; bottom: 0; height: 22px;
    background: rgba(20,20,20,.55); display: flex; justify-content: center; align-items: center; gap: 4px;
  }
  .share-dot { width: 11px; height: 11px; border-radius: 50%; border: 1px solid rgba(255,255,255,.8); }
  .share-dot.slate { background: #35506b; }
  .share-dot.crimson { background: #c8232c; }
  .share-dot.blue { background: #3b5998; }
  .share-dot.sky { background: #1da1f2; }

  .card-title { margin: 12px 0 0 5px; font-size: 19px; font-weight: 400; color: var(--white); line-height: 1; }
  .card-title .lead { color: var(--red); }
  .card-text { margin: 6px 0 0 5px; font-size: 13px; line-height: 15px; color: var(--caption); width: 178px; }

  .load-more {
    position: absolute; left: 473px; top: 946px; width: 149px; height: 38px;
    background: var(--red); color: var(--white); border-radius: 3px;
    font-size: 23px; font-weight: 500; display: flex; align-items: center; justify-content: center;
  }

  .site-footer { position: absolute; left: 0; bottom: 0; width: 1095px; height: 109px; background: var(--footer); }
  .footer-nav { position: absolute; top: 32px; left: 0; width: 100%; display: flex; justify-content: center; gap: 32px; font-family: "Lobster", cursive; font-size: 16px; color: var(--white); }
  .footer-social { position: absolute; top: 71px; left: 0; width: 100%; display: flex; justify-content: center; gap: 5px; }
  .footer-social span { width: 21px; height: 21px; border-radius: 50%; border: 2px solid var(--white); }
</style>
</head>
<body>
  <div class="backdrop" role="img" aria-label="Softly blurred street scene with bright sky fading into dark buildings"></div>

  <header class="site-header">
    <div class="brand">TheGlowFrame.net</div>
    <nav class="account-nav">
      <span class="item">My Account <svg viewBox="0 0 12 8"><path d="M0 0h12L6 8z" fill="#1f4466"/></svg></span>
      <span class="item">Sign Out <svg viewBox="0 0 12 8"><path d="M0 0h12L6 8z" fill="#1f4466"/></svg></span>
    </nav>
  </header>

  <h1 class="gallery-title">Marlene <span class="surname">Dusktrove</span></h1>

  <main>
    <article class="card" style="left:251px;top:330px">
      <div class="card-frame">
        <div class="card-photo photo-runner" role="img" aria-label="Man sprinting along a country road"></div>
        <svg class="corner-badge" viewBox="0 0 44 30"><path d="M0 0H44V30Z" fill="#0b0b0b"/><path d="M31 9c-1.5-3-6-2-5 1.5 .6 2 5 5 5 5s4.4-3 5-5c1-3.5-3.5-4.5-5-1.5z" fill="#ff0000"/></svg>
        <div class="share-strip"><span class="share-dot slate"></span><span class="share-dot crimson"></span><span class="share-dot blue"></span><span class="share-dot sky"></span></div>
      </div>
      <h2 class="card-title"><span class="lead">Pellentesque</span> accumsan</h2>
      <p class="card-text">Lorem ipsum is a dummy text only. Dolor sit amet, consectetur adipiscing elit.</p>
    </article>

    <article class="card" style="left:457px;top:330px">
      <div class="card-frame">
        <div class="card-photo photo-couple" role="img" aria-label="Couple taking a photo on red rocks under a blue sky"></div>
        <svg class="corner-badge" viewBox="0 0 44 30"><path d="M0 0H44V30Z" fill="#0b0b0b"/><path d="M31 9c-1.5-3-6-2-5 1.5 .6 2 5 5 5 5s4.4-3 5-5c1-3.5-3.5-4.5-5-1.5z" fill="#ff0000"/></svg>
        <div class="share-strip"><span class="share-dot slate"></span><span class="share-dot crimson"></span><span class="share-dot blue"></span><span class="share-dot sky"></span></div>
      </div>
      <h2 class="card-title"><span class="lead">Pellentesque</span> accumsan</h2>
      <p class="card-text">Lorem ipsum is a dummy text only. Dolor sit amet, consectetur adipiscing elit.</p>
    </article>

    <article class="card" style="left:662px;top:330px">
      <div class="card-frame">
        <div class="card-photo photo-garden" role="img" aria-label="Green garden with trees reflected in a pond"></div>
        <svg class="corner-badge" viewBox="0 0 44 30"><path d="M0 0H44V30Z" fill="#0b0b0b"/><path d="M31 9c-1.5-3-6-2-5 1.5 .6 2 5 5 5 5s4.4-3 5-5c1-3.5-3.5-4.5-5-1.5z" fill="#ff0000"/></svg>
        <div class="share-strip"><span class="share-dot slate"></span><span class="share-dot crimson"></span><span class="share-dot blue"></span><span class="share-dot sky"></span></div>
      </div>
      <h2 class="card-title"><span class="lead">Pellentesque</span> accumsan</h2>
      <p class="card-text">Lorem ipsum is a dummy text only. Dolor sit amet, consectetur adipiscing elit.</p>
    </article>

    <article class="card" style="left:251px;top:635px">
      <div class="card-frame">
        <div class="card-photo photo-dog" role="img" aria-label="Father, son and dog at sunset"></div>
        <svg class="corner-badge" viewBox="0 0 44 30"><path d="M0 0H44V30Z" fill="#0b0b0b"/><path d="M31 9c-1.5-3-6-2-5 1.5 .6 2 5 5 5 5s4.4-3 5-5c1-3.5-3.5-4.5-5-1.5z" fill="#ff0000"/></svg>
        <div class="share-strip"><span class="share-dot slate"></span><span class="share-dot crimson"></span><span class="share-dot blue"></span><span class="share-dot sky"></span></div>
      </div>
      <h2 class="card-title"><span class="lead">Pellentesque</span> accumsan</h2>
      <p class="card-text">Lorem ipsum is a dummy text only. Dolor sit amet, consectetur adipiscing elit.</p>
    </article>

    <article class="card" style="left:457px;top:635px">
      <div class="card-frame">
        <div class="card-photo photo-couple" role="img" aria-label="Couple taking a photo on red rocks under a blue sky"></div>
        <svg class="corner-badge" viewBox="0 0 44 30"><path d="M0 0H44V30Z" fill="#0b0b0b"/><path d="M31 9c-1.5-3-6-2-5 1.5 .6 2 5 5 5 5s4.4-3 5-5c1-3.5-3.5-4.5-5-1.5z" fill="#ff0000"/></svg>
        <div class="share-strip"><span class="share-dot slate"></span><span class="share-dot crimson"></span><span class="share-dot blue"></span><span class="share-dot sky"></span></div>
      </div>
      <h2 class="card-title"><span class="lead">Pellentesque</span> accumsan</h2>
      <p class="card-text">Lorem ipsum is a dummy text only. Dolor sit amet, consectetur adipiscing elit.</p>
    </article>

    <article class="card" style="left:662px;top:635px">
      <div class="card-frame">
        <div class="card-photo photo-garden" role="img" aria-label="Green garden with trees reflected in a pond"></div>
        <svg class="corner-badge" viewBox="0 0 44 30"><path d="M0 0H44V30Z" fill="#0b0b0b"/><path d="M31 9c-1.5-3-6-2-5 1.5 .6 2 5 5 5 5s4.4-3 5-5c1-3.5-3.5-4.5-5-1.5z" fill="#ff0000"/></svg>
        <div class="share-strip"><span class="share-dot slate"></span><span class="share-dot crimson"></span><span class="share-dot blue"></span><span class="share-dot sky"></span></div>
      </div>
      <h2 class="card-title"><span class="lead">Pellentesque</span> accumsan</h2>
      <p class="card-text">Lorem ipsum is a dummy text only. Dolor sit amet, consectetur adipiscing elit.</p>
    </article>

    <div class="load-more">Load more</div>
  </main>

  <footer class="site-footer">
    <nav class="footer-nav">
      <span>Home</span><span>Contact</span><span>Pinboard</span><span>Biography</span><span>Award-Exhibitions-Travels</span><span>My way of working</span>
    </nav>
    <div class="footer-social" aria-label="Social links">
      <span></span><span></span><span></span><span></span><span></span>
    </div>
  </footer>
</body>
</html>
```